Facebook and Linkedin banner design for Events Rental Company

Company info: We are an Events Rental Company, specialising in selling and rental of events equipment. The products we have at the moment are inflatable structures, inflatable movie screens, modular building blocks and movie licenses. Some common Unique Selling Point of these products are that they are flexible and environmentally-sustainable .

Partners we work with:
- Harbor Vault: Inflatable structures
- Inflatable movie screens: Skyvane
- Movie licenses- Reelcastplus, QT7 Pictures
- Modular building blocks- manufactured inhouse

Requirements:
- minimalist
- clean
- informative; able to tell what the company does at one glance
- linkedin banner size: 1128px wide x 191px tall
- facebook banner size: 820px wide by 360px tall

Target Market(s)

Events Agencies/ Organisers

Industry/Entity Type

Events Rental

Font styles to use
Serif

Colors

Designer to choose only greyscale colors for use in the design.

Requirements
Must have
• Must show the products we have to offer
Nice to have
• A modern and slick design.
Should not have
• Should not seem too hard-sell by throwing all available products out there

```html
<!DOCTYPE html>
<html lang="en">
<head>
<meta charset="utf-8">
<title>Events Rental Company – Banner</title>
<link rel="stylesheet" href="https://fonts.googleapis.com/css2?family=Cinzel+Decorative&family=Lora:wght@400;700&family=Montserrat:wght@600&display=swap">
<style>
  :root {
    --page: #ececec;
    --ink-dark: #2e2e2e;
    --paper: #ffffff;
    --text-light: #f2f2f2;
    --text-dark: #1c1c1c;
    --photo-mall-a: #3a2a2a;
    --photo-mall-b: #b8322c;
    --photo-dome-a: #d9d6cf;
    --photo-dome-b: #8d9298;
    --photo-park-a: #cfd6d8;
    --photo-park-b: #5d7f3c;
  }
  * { margin: 0; padding: 0; box-sizing: border-box; }
  html, body { width: 1200px; height: 872px; overflow: hidden; background: var(--page); }
  .banner {
    position: absolute; left: 26px; top: 184px;
    width: 820px; height: 360px;
    transform: scale(1.4); transform-origin: top left;
    box-shadow: 0 6px 20px rgba(0,0,0,.18);
    overflow: hidden;
    font-family: "Lora", Georgia, serif;
  }
  .banner-shapes { position: absolute; inset: 0; }
  .brand-title {
    position: absolute; left: 12px; top: 16px;
    font-family: "Cinzel Decorative", "Lora", serif;
    font-size: 22.5px; font-weight: 400; color: var(--text-light); letter-spacing: .2px;
    white-space: nowrap;
  }
  .intro {
    position: absolute; left: 12px; top: 56px; width: 420px;
    font-size: 14.5px; line-height: 20px; color: var(--text-light);
  }
  .section-title {
    position: absolute; left: 12px;
    font-size: 16.5px; font-weight: 700; letter-spacing: .2px;
  }
  .products-title { top: 126px; color: var(--text-dark); }
  .products-list {
    position: absolute; left: 13px; top: 151px; width: 440px;
    font-size: 14px; line-height: 18px; color: var(--text-dark);
  }
  .partners-title { top: 211px; color: var(--text-light); }
  .partners-list {
    position: absolute; left: 11px; top: 235px;
    font-size: 14px; color: var(--text-light); white-space: nowrap;
  }
  .partners-list .sep { margin: 0 9px; }
  .contact {
    position: absolute; top: 276px; display: flex; align-items: center; gap: 14px;
    font-family: "Montserrat", Arial, sans-serif; font-weight: 600;
    font-size: 17.5px; color: var(--ink-dark); white-space: nowrap;
  }
  .contact-phone { left: 18px; }
  .contact-email { left: 242px; }
  .contact svg { display: block; }
  .tagline {
    position: absolute; left: 12px; top: 334px;
    font-size: 13px; font-weight: 700; color: var(--text-light); letter-spacing: .2px;
  }
</style>
</head>
<body>
<div class="banner">
  <svg class="banner-shapes" width="820" height="360" viewBox="0 0 820 360">
    <defs>
      <linearGradient id="darkPanel" x1="0" y1="0" x2="1" y2="1">
        <stop offset="0" stop-color="#2a2a2a"/><stop offset="1" stop-color="#3b3b3b"/>
      </linearGradient>
      <linearGradient id="mallTone" x1="0" y1="0" x2="1" y2="1">
        <stop offset="0" stop-color="var(--photo-mall-a)"/><stop offset=".6" stop-color="var(--photo-mall-b)"/><stop offset="1" stop-color="#5a5a5a"/>
      </linearGradient>
      <linearGradient id="domeTone" x1="0" y1="0" x2="0" y2="1">
        <stop offset="0" stop-color="var(--photo-dome-a)"/><stop offset="1" stop-color="var(--photo-dome-b)"/>
      </linearGradient>
      <linearGradient id="parkTone" x1="0" y1="0" x2="0" y2="1">
        <stop offset="0" stop-color="var(--photo-park-a)"/><stop offset="1" stop-color="var(--photo-park-b)"/>
      </linearGradient>
    </defs>
    <rect width="820" height="360" fill="var(--ink-dark)"/>
    <polygon role="img" aria-label="Photo of a shopping mall entrance decorated for Christmas" points="442,0 820,0 820,10 480,116" fill="url(#mallTone)"/>
    <polygon role="img" aria-label="Photo of an inflatable white dome set with tables and chairs" points="480,116 820,10 820,195 550,266" fill="url(#domeTone)"/>
    <polygon role="img" aria-label="Photo of an inflatable outdoor movie screen on a lawn" points="556,318 820,238 820,360 570,360" fill="url(#parkTone)"/>
    <polygon class="left-panel" points="0,0 442,0 482,118 570,360 0,360" fill="url(#darkPanel)"/>
    <polygon class="band-products" points="0,118 504,118 536,200 0,200" fill="var(--paper)"/>
    <polygon class="band-contact" points="0,267 540,267 556,320 0,320" fill="var(--paper)"/>
  </svg>

  <h1 class="brand-title">Events Rental Company</h1>
  <p class="intro">We are an Events Rental Company, specialising in selling and rental of events equipment.</p>

  <h2 class="section-title products-title">PRODUCTS</h2>
  <p class="products-list">Inflatable structures, inflatable movie screens, modular building blocks and movie licenses</p>

  <h2 class="section-title partners-title">PARTNERS</h2>
  <p class="partners-list">Inflable Structures<span class="sep">|</span>Skyvane<span class="sep">|</span>Reelcastplus, QT7 Pictures</p>

  <div class="contact contact-phone">
    <svg width="34" height="28" viewBox="0 0 34 28" aria-hidden="true">
      <path d="M2 9 Q17 -1 32 9 L30 13 L24 12 L23 8 Q17 6 11 8 L10 12 L4 13 Z" fill="var(--ink-dark)"/>
      <path d="M9 12 L25 12 L31 26 L3 26 Z" fill="var(--ink-dark)"/>
      <circle cx="17" cy="19" r="3.5" fill="var(--paper)"/>
    </svg>
    <span>+130 2468 1357</span>
  </div>
  <div class="contact contact-email">
    <svg width="36" height="34" viewBox="0 0 36 34" aria-hidden="true">
      <path d="M2 14 L18 2 L34 14 L34 33 L2 33 Z" fill="var(--ink-dark)"/>
      <rect x="8" y="7" width="20" height="16" fill="var(--paper)"/>
      <text x="18" y="20" text-anchor="middle" font-family="Arial, sans-serif" font-size="13" font-weight="700" fill="var(--ink-dark)">@</text>
      <path d="M2 14 L18 25 L34 14" fill="none" stroke="var(--paper)" stroke-width="1.6"/>
      <path d="M2 33 L15 22 M34 33 L21 22" stroke="var(--paper)" stroke-width="1.6"/>
    </svg>
    <span>hire@rentevents.com</span>
  </div>

  <p class="tagline">ALL PRODUCTS ARE FLEXIBLE AND ENVIRONMENTALLY-SUSTAINABLE</p>
</div>
</body>
</html>
```